Jolly Paws Business Card Update

I have a business card which I love. I want to keep the same logo, colours, font and style. I want to upgrade the scripting and remove some elements and add others.
On the front side under Services - remove the existing wording and insert - Providing individual coaching strategies to create happy, healthy and social canine companions
Under Rebecca Thornley amend the current wording to read: Qualified in Dog Behavioural Training, Natural Animal Healthcare and Animal Health Science
On the reverse side to remove the web address.

```html
<!DOCTYPE html>
<html lang="en">
<head>
<meta charset="utf-8">
<title>Jolly Paws Business Card</title>
<link href="https://fonts.googleapis.com/css2?family=Arimo:wght@400;700&display=swap" rel="stylesheet">
<style>
  :root {
    --backdrop: #2d2d2d;
    --sky-top: #03a0dc;
    --sky-mid: #0a78c4;
    --navy: #1a3f9a;
    --cream: #ece4c2;
    --cream-text: #f4eed6;
    --red-bright: #ec1e26;
    --red-deep: #6e0b10;
    --ink: #2a2a2a;
    --white: #ffffff;
  }
  * { box-sizing: border-box; margin: 0; padding: 0; }
  html, body {
    width: 1075px; height: 1200px; overflow: hidden;
    background: var(--backdrop);
    font-family: "Arimo", Arial, sans-serif;
  }
  .card {
    position: absolute;
    border-radius: 22px;
    overflow: hidden;
    box-shadow: 3px 4px 2px rgba(0,0,0,0.75);
  }
  /* Front side */
  .card--front { left: 207px; top: 188px; width: 660px; height: 389px; }
  .front-sky {
    position: absolute; left: 0; top: 0; width: 100%; height: 209px;
    background: linear-gradient(180deg, var(--sky-top) 0%, var(--sky-mid) 100%);
  }
  .brand-seal {
    position: absolute; left: 80px; top: 51px; width: 138px; height: 138px;
    border-radius: 50%; background: var(--red-bright);
    display: flex; align-items: center; justify-content: center;
  }
  .brand-seal__name { color: var(--cream-text); font-size: 21px; font-weight: 700; }
  .front-divider {
    position: absolute; left: 237px; top: 60px; width: 1.5px; height: 116px;
    background: rgba(255,255,255,0.8);
  }
  .services { position: absolute; left: 260px; top: 68px; color: var(--white); }
  .services__title { font-size: 19px; margin-bottom: 14px; letter-spacing: 0.2px; }
  .services__text { font-size: 17px; line-height: 20.7px; }
  .mission-band {
    position: absolute; left: 0; top: 209px; width: 100%; height: 25px;
    background: var(--cream); color: var(--ink);
    font-size: 16.5px; text-align: center; line-height: 25px;
  }
  .front-red {
    position: absolute; left: 0; top: 234px; width: 100%; height: 155px;
    background: linear-gradient(90deg, var(--red-deep) 0%, var(--red-bright) 52%, var(--red-deep) 100%);
  }
  .person {
    position: absolute; right: 304px; top: 41px; text-align: right; color: var(--white);
  }
  .person__name { font-size: 24px; line-height: 28px; margin-bottom: 2px; }
  .person__credentials { font-size: 16.5px; line-height: 20.7px; }
  .red-divider {
    position: absolute; left: 367px; top: 52px; width: 1.5px; height: 70px;
    background: rgba(255,255,255,0.85);
  }
  .contact { position: absolute; left: 376px; top: 62px; color: var(--white); font-size: 18.5px; }
  .contact__row { display: flex; align-items: center; height: 25px; }
  .contact__icon { width: 18px; height: 18px; margin-right: 9px; flex: none; }
  /* Back side */
  .card--back {
    left: 206px; top: 637px; width: 662px; height: 396px;
    background: linear-gradient(180deg, var(--sky-top) 0%, var(--sky-mid) 45%, var(--navy) 90%);
  }
  .back-seal {
    position: absolute; left: 229px; top: 55px; width: 194px; height: 194px;
    border-radius: 50%; background: var(--red-bright);
  }
  .back-name {
    position: absolute; left: 0; top: 252px; width: 100%; text-align: center;
    color: var(--cream-text); font-size: 52px; font-weight: 700; letter-spacing: 1px;
  }
  .back-wave { position: absolute; left: 0; bottom: 0; width: 662px; height: 80px; }
  .tagline {
    position: absolute; left: 0; top: 358px; width: 100%; text-align: center;
    color: var(--white); font-size: 19px; letter-spacing: 0.3px;
  }
</style>
</head>
<body>
  <section class="card card--front">
    <div class="front-sky">
      <div class="brand-seal"><span class="brand-seal__name">Jolly Paws</span></div>
      <div class="front-divider"></div>
      <div class="services">
        <h2 class="services__title">SERVICES</h2>
        <p class="services__text">Providing individual coaching<br>strategies to create happy,<br>healthy and social canine companions</p>
      </div>
    </div>
    <div class="mission-band">Promoting communication and connection between dogs and their families</div>
    <div class="front-red">
      <div class="person">
        <h1 class="person__name">Rebecca Thornley</h1>
        <p class="person__credentials">Qualified in Dog Behavioural Training,<br>Natural Animal Healthcare and<br>Animal Health Science</p>
      </div>
      <div class="red-divider"></div>
      <div class="contact">
        <div class="contact__row">
          <svg class="contact__icon" viewBox="0 0 18 18" aria-hidden="true">
            <circle cx="9" cy="9" r="8.5" fill="#fff"/>
            <rect x="6" y="4" width="6" height="10" rx="1.2" fill="none" stroke="#b3151b" stroke-width="1.4"/>
            <circle cx="9" cy="12" r="0.8" fill="#b3151b"/>
          </svg>
          <span>0412 784 205</span>
        </div>
        <div class="contact__row">
          <svg class="contact__icon" viewBox="0 0 18 18" aria-hidden="true">
            <circle cx="9" cy="9" r="8.5" fill="#fff"/>
            <rect x="4.5" y="6" width="9" height="6.5" fill="none" stroke="#b3151b" stroke-width="1.3"/>
            <path d="M4.5 6 L9 9.8 L13.5 6" fill="none" stroke="#b3151b" stroke-width="1.3"/>
          </svg>
          <span>hello@jollypawscoaching.com</span>
        </div>
      </div>
    </div>
  </section>

  <section class="card card--back">
    <div class="back-seal"></div>
    <div class="back-name">JOLLY PAWS</div>
    <svg class="back-wave" viewBox="0 0 662 80" preserveAspectRatio="none" aria-hidden="true">
      <defs>
        <linearGradient id="waveRed" x1="0" x2="1" y1="0" y2="0">
          <stop offset="0" stop-color="#6e0b10"/>
          <stop offset="0.52" stop-color="#ec1e26"/>
          <stop offset="1" stop-color="#6e0b10"/>
        </linearGradient>
      </defs>
      <path d="M0 41 Q331 -20 662 36 L662 80 L0 80 Z" fill="url(#waveRed)"/>
      <path d="M0 41 Q331 -20 662 36" fill="none" stroke="#fff" stroke-width="3"/>
    </svg>
    <div class="tagline">HAPPY DOGS, HAPPY OWNERS</div>
  </section>
</body>
</html>
```